E-commerce Website Trevalin.com

Work Required
Homepage: Creation of an attractive design, clearly presenting product categories (recovery mixes, detox, etc., herbal candies).
Product Page: Highlight products with detailed information, use of mockups to represent the products.
Logo: Design a logo representative of Trevalin.com, naturally evoking the equestrian field and the organic aspect of the products.

Target Market(s)

show pdf in documents

Industry/Entity Type

show pdf in documents

Coding

Coded - Design and coding required

Requirements
Must have
• show pdf in documents
Nice to have
• show pdf in documents
Should not have
• show pdf in documents

```html
<!DOCTYPE html>
<html lang="en">
<head>
<meta charset="utf-8">
<title>Trevalin – Organic Horse Food</title>
<link href="https://fonts.googleapis.com/css2?family=Montserrat:wght@400;500;600;700;800&display=swap" rel="stylesheet">
<style>
:root{
  --orange:#c0622c;
  --orange-dark:#a14f22;
  --brown:#8a3f17;
  --beige:#f4eee1;
  --ink:#222;
  --muted:#555;
  --line:#e2e2e2;
  --green-soft:#dcebd6;
  --cream:#f4ede1;
  --white:#fff;
  --black:#000;
}
*{box-sizing:border-box;margin:0;padding:0}
html,body{width:1200px;height:5195px;overflow:hidden}
body{font-family:'Montserrat',sans-serif;color:var(--ink);background:var(--white);position:relative}
.abs{position:absolute}
.btn-outline{position:absolute;border:1.5px solid var(--orange);border-radius:20px;background:var(--white);font-size:11px;color:var(--ink);display:flex;align-items:center;justify-content:center}
.section-title{position:absolute;left:0;width:1200px;display:flex;justify-content:center;align-items:center;gap:16px;font-weight:700;font-size:41px;color:var(--orange);letter-spacing:1px}
.section-title::before,.section-title::after{content:"";width:54px;height:4px;background:var(--orange)}
.circle-arrow{position:absolute;width:30px;height:30px;border:1.5px solid var(--ink);border-radius:50%;display:flex;align-items:center;justify-content:center}

/* top bar */
.topbar{position:absolute;top:0;left:0;width:1200px;height:31px;background:var(--orange-dark);color:var(--white);font-size:13px;letter-spacing:.5px}
.topbar .msg{position:absolute;left:0;width:1200px;top:8px;text-align:center}
/* header */
.header{position:absolute;top:31px;left:0;width:1200px;height:110px;border-bottom:1px solid var(--line)}
.brand{position:absolute;left:38px;top:38px;display:flex;align-items:center;gap:8px;color:var(--orange);font-weight:700;font-size:17px;letter-spacing:.5px}
.brand .dot{width:26px;height:26px;border-radius:50%;background:var(--orange)}
.search{position:absolute;left:240px;top:37px;width:640px;height:42px;border:1px solid #ccc;border-radius:22px;font-size:11px;padding:14px 0 0 44px;color:#333}
.account{position:absolute;left:889px;top:37px;width:123px;height:42px;border:1.5px solid var(--orange);border-radius:22px;color:var(--orange);font-size:12px;display:flex;align-items:center;justify-content:center;gap:8px}
.cart{position:absolute;left:1022px;top:37px;width:131px;height:42px;background:var(--orange);border-radius:22px;color:var(--white);font-size:12px;font-weight:600;display:flex;align-items:center;justify-content:center;gap:16px}
.nav{position:absolute;top:141px;left:0;width:1200px;height:66px;border-bottom:1px solid var(--line);font-size:15px;letter-spacing:.5px}
.nav span{position:absolute;top:24px;transform:translateX(-50%)}
/* hero */
.hero{position:absolute;top:207px;left:0;width:1200px;height:613px;background:linear-gradient(100deg,#0d0a07 0%,#1f140b 40%,#4a3420 70%,#8b7557 85%,#5a4025 100%)}
.hero h1{position:absolute;left:34px;top:180px;color:var(--white);font-size:43px;font-weight:700;line-height:48px;letter-spacing:1.5px}
.hero p{position:absolute;left:36px;top:296px;color:var(--white);font-size:14px;line-height:21px;width:440px}
.hero .shop{position:absolute;left:38px;top:371px;width:179px;height:53px;background:var(--white);border-radius:28px;font-size:20px;font-weight:500;display:flex;align-items:center;justify-content:center}
/* product cards */
.pcard{position:absolute;background:var(--white);border:1px solid #e6e6e6;border-radius:6px;box-shadow:0 2px 8px rgba(0,0,0,.07)}
.pcard .tag{position:absolute;right:20px;top:28px;background:var(--orange);color:var(--white);font-size:10px;padding:3px 6px}
.pcard .img{position:absolute;left:50%;transform:translateX(-50%);border-radius:50%}
.pcard .price{position:absolute;left:30px;font-size:17px}
.pcard .name{position:absolute;left:30px;font-size:18px;font-weight:500;letter-spacing:.5px}
.pcard .stars{position:absolute;left:30px;font-size:13px;letter-spacing:2px}
.pcard .stars small{font-size:10px;letter-spacing:0;margin-left:16px}
.pcard .note{position:absolute;left:30px;font-size:12px}
.pcard .avail{position:absolute;left:30px;font-size:10.5px;line-height:18px;width:200px;color:#333}
.hay{background:radial-gradient(circle at 40% 40%,#a8a052,#6b6c2a 60%,#3e4218)}
.pellet{background:radial-gradient(circle at 45% 45%,#4a5a30,#283319 60%,#151d0d)}
.treat{background:radial-gradient(circle at 45% 45%,#a6803e,#6b4e22 60%,#3a2a12)}
.view-all{position:absolute;left:510px;top:1539px;width:180px;height:52px;background:var(--orange);color:var(--white);border-radius:28px;font-size:20px;font-weight:500;display:flex;align-items:center;justify-content:center;letter-spacing:1px}
/* fresh food */
.fresh{position:absolute;top:1678px;left:0;width:1200px;height:742px;background:var(--beige)}
.fresh .photo{position:absolute;left:38px;top:172px;width:1124px;height:482px;background:linear-gradient(90deg,#6c8a3a 0%,#7b9a46 40%,#9b8b6e 55%,#a08c70 100%)}
.fresh .pcard .tag{background:#1f3a1a}
.fresh .arrow{position:absolute;width:28px;height:28px;border-radius:50%;background:var(--orange);display:flex;align-items:center;justify-content:center}
/* hot deals */
.deal{position:absolute;top:2586px;width:339px;height:510px;background:var(--white);border-radius:6px;box-shadow:0 2px 8px rgba(0,0,0,.1);text-align:center}
.deal .img{height:292px;border-radius:6px 6px 0 0}
.deal .kicker{margin-top:24px;font-size:15px}
.deal h3{margin-top:14px;font-size:21px;font-weight:700;letter-spacing:1px}
.deal p{margin-top:16px;font-size:15px;line-height:27px;color:#333}
.deal .btn-outline{left:104px;top:456px;width:106px;height:28px}
/* category */
.category{position:absolute;top:3237px;left:0;width:1200px;height:519px;background:var(--beige)}
.cat{position:absolute;top:174px;width:176px;height:206px;background:var(--white);border-radius:6px;box-shadow:0 2px 8px rgba(0,0,0,.06);text-align:center}
.cat .img{position:absolute;left:42px;top:16px;width:92px;height:92px;border-radius:50%;box-shadow:0 14px 20px rgba(0,0,0,.12)}
.cat .label{position:absolute;left:0;top:140px;width:176px;font-size:14px;font-weight:700;line-height:20px;letter-spacing:.5px}
/* our products */
.products-title{position:absolute;left:38px;top:3826px;display:flex;align-items:center;gap:16px;font-weight:700;font-size:41px;color:var(--orange);letter-spacing:1px}
.products-title::before,.products-title::after{content:"";width:54px;height:4px;background:var(--orange)}
.mock{position:absolute;border:1px solid #ddd;background:linear-gradient(135deg,#f1f1f1,#e3e3e3)}
.mock.selected{border:4px solid var(--orange)}
.mock .pack{position:absolute;left:50%;top:50%;transform:translate(-50%,-50%)}
.detail{position:absolute;left:652px;top:3906px;width:460px}
.detail h2{font-size:31px;font-weight:500;letter-spacing:1px}
.detail .desc{margin-top:14px;font-size:15px;line-height:27px;color:#444;letter-spacing:.3px}
.detail .style{margin-top:12px;font-size:12px}
.chip{position:absolute;height:28px;border:1.5px solid #333;border-radius:16px;font-size:11px;display:flex;align-items:center;justify-content:center}
.price-big{position:absolute;left:645px;top:4118px;font-size:33px;font-weight:500}
.was{position:absolute;left:752px;top:4128px;font-size:11px;line-height:13px}
.was s{text-decoration:line-through}
.qty-btn{position:absolute;top:4196px;width:38px;height:38px;border:1.5px solid var(--orange);border-radius:50%;color:var(--orange);font-size:22px;display:flex;align-items:center;justify-content:center}
/* lifestyle */
.lifestyle{position:absolute;top:4331px;left:0;width:1200px;height:584px;background:var(--beige)}
.life{position:absolute;top:167px;width:229px;height:333px;background:var(--white);box-shadow:0 2px 8px rgba(0,0,0,.08);text-align:center}
.life .ic{position:absolute;left:49px;top:22px;width:130px;height:130px;border-radius:50%;display:flex;align-items:center;justify-content:center;box-shadow:0 10px 18px rgba(0,0,0,.12)}
.life .label{position:absolute;left:0;top:174px;width:229px;font-size:15px;font-weight:600;line-height:20px;letter-spacing:.5px}
.life .text{position:absolute;left:10px;top:236px;width:209px;font-size:12px;line-height:21px}
/* footer */
.footer{position:absolute;top:4915px;left:0;width:1200px;height:280px;background:var(--black);color:var(--white)}
.footer .brand{left:0;top:50px;width:1200px;justify-content:center;color:var(--white)}
.footer .brand .dot{background:var(--white)}
.fnav{position:absolute;top:166px;left:0;width:1200px;font-size:16px;letter-spacing:.5px}
.fnav span{position:absolute;transform:translateX(-50%)}
.fnav i{position:absolute;top:-2px;width:2px;height:22px;background:var(--white)}
.footer .rule{position:absolute;left:66px;top:216px;width:1002px;height:1px;background:#888}
.footer .copy{position:absolute;left:0;top:244px;width:1200px;text-align:center;font-size:16px;letter-spacing:.5px}
</style>
</head>
<body>

<div class="topbar">
  <svg class="abs" style="left:285px;top:9px" width="8" height="13" viewBox="0 0 8 13"><path d="M7 1 2 6.5 7 12" fill="none" stroke="#fff" stroke-width="1.6"/></svg>
  <div class="msg">Because their well-being is your priority - 100% Made in France</div>
  <svg class="abs" style="left:904px;top:9px" width="8" height="13" viewBox="0 0 8 13"><path d="M1 1l5 5.5L1 12" fill="none" stroke="#fff" stroke-width="1.6"/></svg>
  <div class="abs" style="left:1076px;top:8px">English</div>
  <svg class="abs" style="left:1143px;top:11px" width="13" height="8" viewBox="0 0 13 8"><path d="M1 1l5.5 5L12 1" fill="none" stroke="#fff" stroke-width="1.6"/></svg>
</div>

<header class="header">
  <div class="brand"><span class="dot"></span>TREVALIN</div>
  <div class="search">Search For...</div>
  <div class="account">
    <svg width="16" height="16" viewBox="0 0 16 16"><circle cx="8" cy="5" r="3.2" fill="none" stroke="#c0622c" stroke-width="1.4"/><path d="M2 15c0-3.5 2.7-5.5 6-5.5s6 2 6 5.5" fill="none" stroke="#c0622c" stroke-width="1.4"/></svg>
    Account
  </div>
  <div class="cart">
    <svg width="24" height="20" viewBox="0 0 24 20"><path d="M1 1h4l3 12h12l3-9H7" fill="none" stroke="#fff" stroke-width="1.6"/><circle cx="9" cy="17" r="1.6" fill="#fff"/><circle cx="19" cy="17" r="1.6" fill="#fff"/></svg>
    $0.55
  </div>
</header>

<nav class="nav">
  <span style="left:84px">HOME</span>
  <span style="left:219px">CATEGORIES</span>
  <span style="left:372px">ABOUT US</span>
  <span style="left:525px">OUR STORES</span>
  <span style="left:670px">RECIPES</span>
  <span style="left:786px">BLOG</span>
  <span style="left:883px">FAQ</span>
  <span style="left:979px">CART</span>
  <span style="left:1099px">CONTACT</span>
</nav>

<section class="hero" role="img" aria-label="White horse eating hay in a dark wooden stable">
  <h1>WELCOME TO<br>TREVALIN</h1>
  <p>Lorem Ipsum is simply dummy text of the printing and typesetting industry.</p>
  <div class="shop">SHOP</div>
</section>

<!-- Best sellers -->
<div class="section-title" style="top:896px">BEST SELLERS</div>

<div class="pcard" style="left:36px;top:988px;width:257px;height:495px">
  <span class="tag">NEW</span>
  <div class="img hay" style="top:82px;width:156px;height:156px" role="img" aria-label="Dried hay mix"></div>
  <div class="price" style="top:284px">$9.00</div>
  <div class="name" style="top:312px">Hay&nbsp; Horse Foods</div>
  <div class="stars" style="top:342px">☆☆☆☆☆<small>(5.0)</small></div>
  <div class="note" style="top:368px">No added salt!</div>
  <div class="btn-outline" style="left:30px;top:396px;width:106px;height:28px">Buy now</div>
  <div class="avail" style="top:432px">Choose a store to see local availability</div>
</div>
<div class="pcard" style="left:327px;top:988px;width:257px;height:495px">
  <span class="tag">NEW</span>
  <div class="img pellet" style="top:82px;width:156px;height:156px" role="img" aria-label="Dark hay pellets"></div>
  <div class="price" style="top:284px">$9.00</div>
  <div class="name" style="top:312px">Hay&nbsp; Horse Foods</div>
  <div class="stars" style="top:342px">☆☆☆☆☆<small>(5.0)</small></div>
  <div class="note" style="top:368px">No added salt!</div>
  <div class="btn-outline" style="left:30px;top:396px;width:106px;height:28px">Buy now</div>
  <div class="avail" style="top:432px">Choose a store to see local availability</div>
</div>
<div class="pcard" style="left:617px;top:988px;width:257px;height:495px">
  <span class="tag">NEW</span>
  <div class="img treat" style="top:82px;width:156px;height:156px" role="img" aria-label="Crunchy horse treats"></div>
  <div class="price" style="top:284px">$9.00</div>
  <div class="name" style="top:312px">TREATS&nbsp; Horse Foods</div>
  <div class="stars" style="top:342px">☆☆☆☆☆<small>(5.0)</small></div>
  <div class="note" style="top:368px">No added salt!</div>
  <div class="btn-outline" style="left:30px;top:396px;width:106px;height:28px">Buy now</div>
  <div class="avail" style="top:432px">Choose a store to see local availability</div>
</div>
<div class="pcard" style="left:907px;top:988px;width:257px;height:495px">
  <span class="tag">NEW</span>
  <div class="img hay" style="top:82px;width:156px;height:156px" role="img" aria-label="Dried herb mix"></div>
  <div class="price" style="top:284px">$9.00</div>
  <div class="name" style="top:312px">TREATS&nbsp; Horse Foods</div>
  <div class="stars" style="top:342px">☆☆☆☆☆<small>(5.0)</small></div>
  <div class="note" style="top:368px">No added salt!</div>
  <div class="btn-outline" style="left:30px;top:396px;width:106px;height:28px">Buy now</div>
  <div class="avail" style="top:432px">Choose a store to see local availability</div>
</div>

<div class="view-all">VIEW ALL</div>

<!-- Fresh food -->
<section class="fresh">
  <div class="section-title" style="top:86px">SHOP FRESH FOOD</div>
  <div class="photo" role="img" aria-label="Young foal in a grassy paddock next to a yellow bucket"></div>
  <div class="pcard" style="left:595px;top:190px;width:254px;height:427px">
    <span class="tag">NEW</span>
    <div class="img hay" style="top:74px;width:156px;height:148px" role="img" aria-label="Dried hay mix"></div>
    <div class="price" style="top:256px">$9.00</div>
    <div class="name" style="top:290px">Hay&nbsp; Horse Foods</div>
    <div class="stars" style="top:332px">☆☆☆☆☆<small>(5.0)</small></div>
    <div class="btn-outline" style="left:30px;top:368px;width:106px;height:28px">Buy now</div>
  </div>
  <div class="pcard" style="left:855px;top:190px;width:254px;height:427px">
    <span class="tag">NEW</span>
    <div class="img hay" style="top:74px;width:156px;height:148px" role="img" aria-label="Dried hay mix"></div>
    <div class="price" style="top:256px">$9.00</div>
    <div class="name" style="top:290px">Hay&nbsp; Horse Foods</div>
    <div class="stars" style="top:332px">☆☆☆☆☆<small>(5.0)</small></div>
    <div class="btn-outline" style="left:30px;top:368px;width:106px;height:28px">Buy now</div>
  </div>
  <div class="arrow" style="left:555px;top:390px"><svg width="10" height="12" viewBox="0 0 10 12"><path d="M7 1 2 6l5 5" fill="none" stroke="#fff" stroke-width="1.6"/></svg></div>
  <div class="arrow" style="left:1116px;top:390px"><svg width="10" height="12" viewBox="0 0 10 12"><path d="M3 1l5 5-5 5" fill="none" stroke="#fff" stroke-width="1.6"/></svg></div>
</section>

<!-- Hot deals -->
<div class="section-title" style="top:2496px">HOT DEALS</div>
<div class="deal" style="left:38px">
  <div class="img" style="background:linear-gradient(160deg,#c9a06a,#8d6336 60%,#b58a55)" role="img" aria-label="Pile of oat grains"></div>
  <div class="kicker">Fresh Everyday</div><h3>FINEST BREAD</h3>
  <p>Organic grasses are a great<br>option for horses because they</p>
  <div class="btn-outline">Buy now</div>
</div>
<div class="deal" style="left:430px">
  <div class="img" style="background:linear-gradient(160deg,#4e7d35,#2f5a22 60%,#6a6a5a)" role="img" aria-label="Fresh herbs growing in a wooden planter"></div>
  <div class="kicker">Fresh Everyday</div><h3>FINEST BREAD</h3>
  <p>Organic grasses are a great<br>option for horses because they</p>
  <div class="btn-outline">Buy now</div>
</div>
<div class="deal" style="left:823px">
  <div class="img" style="background:linear-gradient(135deg,#c7782a,#a52a36 45%,#2a2420 70%,#9a8a4a)" role="img" aria-label="Wooden trays of colourful dried spices and seeds"></div>
  <div class="kicker">Fresh Everyday</div><h3>FINEST BREAD</h3>
  <p>Organic grasses are a great<br>option for horses because they</p>
  <div class="btn-outline">Buy now</div>
</div>
<div class="circle-arrow" style="left:555px;top:3135px"><svg width="14" height="12" viewBox="0 0 14 12"><path d="M13 6H2M6 1 1 6l5 5" fill="none" stroke="#222" stroke-width="1.5"/></svg></div>
<div class="circle-arrow" style="left:615px;top:3135px"><svg width="14" height="12" viewBox="0 0 14 12"><path d="M1 6h11M8 1l5 5-5 5" fill="none" stroke="#222" stroke-width="1.5"/></svg></div>

<!-- Category -->
<section class="category">
  <div class="section-title" style="top:77px">SHOP BY CATEGORY</div>
  <div class="cat" style="left:38px"><div class="img" style="background:radial-gradient(circle,#1f5a3c,#0f3a25)" role="img" aria-label="Spirulina powder"></div><div class="label">ORGANIC<br>SPIRULINA</div></div>
  <div class="cat" style="left:228px"><div class="img" style="background:radial-gradient(circle,#f3e6c8,#dcc79c)" role="img" aria-label="Granulated grain"></div><div class="label">ORGANIC<br>GRANULATED</div></div>
  <div class="cat" style="left:418px"><div class="img" style="background:radial-gradient(circle,#9a9a8a,#4a4a40)" role="img" aria-label="Dried herb mix"></div><div class="label">ORGANIC<br>SPIRULINA</div></div>
  <div class="cat" style="left:607px"><div class="img" style="background:radial-gradient(circle,#c8c070,#8c8a3a)" role="img" aria-label="Dried meadowsweet"></div><div class="label">MEADOWSWEET<br>ORGANIC</div></div>
  <div class="cat" style="left:797px"><div class="img" style="background:radial-gradient(circle,#a8b890,#6c7f56)" role="img" aria-label="Dried dandelion leaves"></div><div class="label">DANDELION<br>ORGANIC</div></div>
  <div class="cat" style="left:986px"><div class="img" style="background:radial-gradient(circle,#d49a62,#9a5a2e)" role="img" aria-label="Fenugreek seeds"></div><div class="label">ORGANIC<br>FENUGREEK</div></div>
  <div class="circle-arrow" style="left:555px;top:392px"><svg width="14" height="12" viewBox="0 0 14 12"><path d="M13 6H2M6 1 1 6l5 5" fill="none" stroke="#222" stroke-width="1.5"/></svg></div>
  <div class="circle-arrow" style="left:615px;top:392px"><svg width="14" height="12" viewBox="0 0 14 12"><path d="M1 6h11M8 1l5 5-5 5" fill="none" stroke="#222" stroke-width="1.5"/></svg></div>
</section>

<!-- Our products -->
<div class="products-title">OUR PRODUCTS</div>
<div class="mock" style="left:38px;top:3913px;width:269px;height:329px">
  <div class="pack" style="width:128px;height:200px;border-radius:10px;background:linear-gradient(90deg,#c9a987,#e0c6a6 50%,#c4a27f)" role="img" aria-label="Kraft paper feed bag mockup"></div>
</div>
<div class="mock selected" style="left:345px;top:3909px;width:270px;height:333px">
  <div class="pack" style="width:150px;height:170px;border-radius:10px 10px 40px 40px;background:linear-gradient(90deg,#d9d9d9,#ffffff 45%,#d4d4d4)" role="img" aria-label="White plastic tub mockup"></div>
</div>
<div class="detail">
  <h2>Keto Crunch</h2>
  <div class="desc">Keto-friendly combination of pecans, almonds,<br>walnuts, pepitas and no sugar added dark chocolate.</div>
  <div class="style">Style</div>
</div>
<div class="chip" style="left:645px;top:4052px;width:106px">Smart Mix</div>
<div class="chip" style="left:760px;top:4054px;width:106px">Student Mix</div>
<div class="price-big">$4.99</div>
<div class="was"><s>$6.00</s><br>you save $1.01</div>
<div class="qty-btn" style="left:645px">−</div>
<div class="abs" style="left:703px;top:4203px;font-size:18px;color:var(--orange)">1</div>
<div class="qty-btn" style="left:736px">+</div>
<div class="abs" style="left:807px;top:4199px;width:128px;height:34px;background:var(--brown);color:#fff;border-radius:18px;font-size:13px;display:flex;align-items:center;justify-content:center">Add to cart</div>
<div class="abs" style="left:954px;top:4199px;width:128px;height:34px;border:1.5px solid #333;border-radius:18px;font-size:13px;display:flex;align-items:center;justify-content:center">Buy it now</div>

<!-- Lifestyle -->
<section class="lifestyle">
  <div class="section-title" style="top:88px">SHOP BY LIFESTYLE</div>
  <div class="life" style="left:38px">
    <div class="ic" style="background:var(--cream)"><svg width="42" height="36" viewBox="0 0 42 36" fill="none" stroke="#333" stroke-width="1.6"><path d="M4 30c0-12 8-20 18-20-1 11-8 18-18 20z"/><path d="M24 24c2-10 8-16 16-16 0 9-6 15-16 16z"/><path d="M4 30l14-14M24 24l10-10"/></svg></div>
    <div class="label">ORGANIC<br>SPIRULINA</div>
    <div class="text">The Magic of Organic Herbs: Personalized Recipes for Your Horse.</div>
  </div>
  <div class="life" style="left:337px">
    <div class="ic" style="background:var(--green-soft)"><svg width="48" height="48" viewBox="0 0 48 48" fill="none" stroke="#333" stroke-width="1.6"><circle cx="24" cy="24" r="20"/><path d="M24 10v30M24 16l-5-4M24 16l5-4M24 24l-6-4M24 24l6-4M24 32l-6-4M24 32l6-4M10 38 38 10"/></svg></div>
    <div class="label">PALEO<br>SPIRULINA</div>
    <div class="text">The Magic of Organic Herbs: Personalized Recipes for Your Horse.</div>
  </div>
  <div class="life" style="left:635px">
    <div class="ic" style="background:var(--cream)"><svg width="36" height="48" viewBox="0 0 36 48" fill="none" stroke="#333" stroke-width="1.6"><path d="M18 4c6 4 8 12 6 22-1 6-3 10-6 14-3-4-5-8-6-14-2-10 0-18 6-22z"/><path d="M18 44V12M4 28c6 0 10 4 14 12M32 28c-6 0-10 4-14 12"/></svg></div>
    <div class="label">KETO<br>SPIRULINA</div>
    <div class="text">The Magic of Organic Herbs: Personalized Recipes for Your Horse.</div>
  </div>
  <div class="life" style="left:930px">
    <div class="ic" style="background:var(--green-soft)"><svg width="48" height="40" viewBox="0 0 48 40" fill="none" stroke="#333" stroke-width="1.6"><path d="M8 30c-6-8 0-24 16-26 14-2 22 8 18 18-4 10-16 16-26 14-4-1-6-3-8-6z"/><ellipse cx="26" cy="18" rx="7" ry="5"/><circle cx="26" cy="18" r="2"/></svg></div>
    <div class="label">PLANT<br>SPIRULINA</div>
    <div class="text">The Magic of Organic Herbs: Personalized Recipes for Your Horse.</div>
  </div>
</section>

<footer class="footer">
  <div class="brand"><span class="dot"></span>TREVALIN</div>
  <div class="fnav">
    <span style="left:164px">HOME</span><i style="left:242px"></i>
    <span style="left:319px">ABOUT US</span><i style="left:407px"></i>
    <span style="left:509px">OUR SERVICES</span><i style="left:598px"></i>
    <span style="left:661px">SHOP</span><i style="left:738px"></i>
    <span style="left:781px">NEWS</span><i style="left:867px"></i>
    <span style="left:920px">CONTACT</span>
  </div>
  <div class="rule"></div>
  <div class="copy">Copyright © 2024&nbsp; Trevalin. All Rights Reserved</div>
</footer>

</body>
</html>
```